Card Design to Advertise New Business

I am looking to have a card designed so that I can pass it out to help promote my business. I have never done this before so I honestly do not know where to start with any ideas. I am providing my website address to help. I provide math tutoring, test prep, and schooling options.

I am looking for a card bigger than a business card but smaller than a flyer. Something front and back that I can pass out.

Business Information
Phone: 470-555-0192
Website: www.kelvanostudyhall.example
Address: 418 Brackenfield Rd Ste 340 Marietta GA 30072
Email: kelvanoservices@kelvanomail.example

Services:
Math Tutoring
NEQ & BOW Test Prep
Group and Private Sessions
Fully Accredited Private School

Target Market(s)

Middle and High School Students

Industry/Entity Type

Education

Requirements
Must have
• Information from my website

```html
<!DOCTYPE html>
<html lang="en">
<head>
<meta charset="utf-8">
<title>Kelvano Study Hall – Promo Card</title>
<link rel="stylesheet" href="https://fonts.googleapis.com/css2?family=Fredoka:wght@600;700&family=Roboto+Condensed:wght@400;500&display=swap">
<style>
  :root {
    --stage: #e3e3e3;
    --navy: #27225c;
    --white: #ffffff;
    --yellow: #f2e600;
    --green: #3fae2a;
    --blue: #28a3df;
    --red: #e3151d;
    --orange: #f7941d;
    --band: #c4361c;
    --head: "Fredoka", "Arial Rounded MT Bold", sans-serif;
    --body: "Roboto Condensed", "Arial Narrow", sans-serif;
  }
  * { box-sizing: border-box; margin: 0; padding: 0; }
  html, body { width: 1200px; height: 1200px; overflow: hidden; background: var(--stage); }
  .stage { position: relative; width: 1200px; height: 1200px; }

  .card {
    position: absolute; top: 276px; width: 432px; height: 648px;
    background: var(--navy); overflow: hidden;
    box-shadow: 0 4px 10px rgba(0,0,0,.25);
  }
  .card--front { left: 112px; }
  .card--back { left: 647px; }

  /* front */
  .headline {
    position: absolute; left: 30px; top: 26px;
    font-family: var(--head); font-weight: 700; font-size: 24px; line-height: 27.5px;
    text-transform: uppercase; letter-spacing: .3px; font-kerning: none;
  }
  .headline span { display: block; }
  .headline .c-yellow { color: var(--yellow); }
  .headline .c-green { color: var(--green); }
  .headline .c-blue { color: var(--blue); }
  .headline .c-red { color: var(--red); }
  .headline .c-orange { color: var(--orange); }
  .rule { position: absolute; height: 3px; width: 84px; background: var(--white); }
  .headline-rule { left: 30px; top: 166px; }

  .brand-box {
    position: absolute; left: 267px; top: 0; width: 135px; height: 149px;
    background: var(--white);
    display: flex; flex-direction: column; align-items: center; justify-content: center; gap: 10px;
  }
  .brand-dot { width: 62px; height: 62px; border-radius: 50%; background: var(--blue); }
  .brand-name {
    font-family: var(--head); font-weight: 700; font-size: 15px; line-height: 16px;
    color: var(--navy); text-align: center; text-transform: uppercase;
  }

  .art { position: absolute; border-radius: 14px; }
  .art--desk {
    left: 20px; top: 180px; width: 372px; height: 318px;
    background: radial-gradient(ellipse at 50% 60%, #6a6aa8 0%, #3d3a7a 55%, rgba(39,34,92,0) 80%);
  }

  .phone {
    position: absolute; left: 30px; top: 524px;
    display: flex; align-items: center; gap: 12px;
    font-family: var(--head); font-weight: 700; font-size: 53px; line-height: 1;
    color: var(--white); letter-spacing: .5px;
  }
  .phone svg { width: 40px; height: 40px; }
  .address {
    position: absolute; right: 30px; top: 579px;
    display: flex; align-items: center; gap: 6px;
    font-family: var(--body); font-weight: 500; font-size: 11.5px; color: var(--white);
  }
  .address svg { width: 13px; height: 15px; }

  .contact-band {
    position: absolute; left: 0; top: 604px; width: 100%; height: 24px;
    background: var(--band);
    display: flex; align-items: center; justify-content: center; gap: 16px;
    font-family: var(--body); font-size: 11px; color: var(--white);
  }
  .contact-band .item { display: flex; align-items: center; gap: 6px; white-space: nowrap; }
  .contact-band svg { width: 14px; height: 14px; }

  /* back */
  .section-title {
    position: absolute; left: 0; top: 22px; width: 100%; text-align: center;
    font-family: var(--head); font-weight: 700; font-size: 27px; color: var(--green);
    text-transform: uppercase; letter-spacing: .3px;
  }
  .title-rule { left: 174px; top: 57px; }

  .service {
    position: absolute; width: 216px; text-align: center;
    font-family: var(--head); font-weight: 700; font-size: 19.5px; line-height: 20px;
    color: var(--white); text-transform: uppercase;
    letter-spacing: .4px; font-kerning: none;
  }
  .service svg { display: block; margin: 0 auto 14px; width: 42px; height: 42px; }
  .service--math { left: -4px; top: 104px; }
  .service--prep { left: 212px; top: 102px; }
  .service--group { left: -4px; top: 220px; }
  .service--school { left: 212px; top: 218px; }

  .art--study {
    left: 44px; top: 354px; width: 348px; height: 238px;
    border-radius: 60px 80px 40px 70px;
    background: linear-gradient(160deg, #4c4d8c 0%, #45468a 60%, #3a3a7c 100%);
  }
</style>
</head>
<body>
<main class="stage">

  <section class="card card--front" aria-label="Card front">
    <h1 class="headline">
      <span class="c-yellow">Study</span>
      <span class="c-green">Coaching</span>
      <span class="c-blue">and Math</span>
      <span class="c-red">Tutoring</span>
      <span class="c-orange">for all ages</span>
    </h1>
    <div class="rule headline-rule"></div>

    <div class="brand-box">
      <div class="brand-dot"></div>
      <div class="brand-name">Kelvano<br>Study Hall</div>
    </div>

    <div class="art art--desk" role="img" aria-label="Illustration of a math desk with calculator, coffee mug, pencil cup, rulers, set square and hand-written formulas"></div>

    <div class="phone">
      <svg viewBox="0 0 24 24" aria-hidden="true"><path fill="#e3151d" d="M6.6 2.5c.6-.4 1.4-.3 1.8.3l2.3 3.3c.4.6.3 1.4-.2 1.9L9 9.4c.9 2 2.6 3.8 4.6 4.7l1.4-1.5c.5-.5 1.3-.6 1.9-.2l3.3 2.3c.6.4.7 1.2.3 1.8l-1.4 2.2c-.6.9-1.7 1.3-2.7 1C9.9 18 6 14.1 4.2 7.6c-.3-1 .1-2.1 1-2.7z"/></svg>
      470-555-0192
    </div>
    <div class="address">
      <svg viewBox="0 0 12 16" aria-hidden="true"><path fill="#3fae2a" d="M6 0a6 6 0 0 0-6 6c0 4.5 6 10 6 10s6-5.5 6-10a6 6 0 0 0-6-6zm0 8.5A2.5 2.5 0 1 1 6 3.5a2.5 2.5 0 0 1 0 5z"/></svg>
      418 Brackenfield Rd Ste 340 Marietta GA 30072
    </div>

    <div class="contact-band">
      <span class="item">
        <svg viewBox="0 0 16 16" aria-hidden="true"><g fill="none" stroke="#f2e600" stroke-width="1.2"><circle cx="8" cy="8" r="7"/><ellipse cx="8" cy="8" rx="3" ry="7"/><path d="M1 8h14M2.2 4.5h11.6M2.2 11.5h11.6"/></g></svg>
        www.kelvanostudyhall.example
      </span>
      <span class="item">
        <svg viewBox="0 0 16 16" aria-hidden="true"><rect x="1" y="3" width="14" height="10" fill="#f2e600"/><path d="M1 3l7 6 7-6M1 13l5-5M15 13l-5-5" fill="none" stroke="#c4361c" stroke-width="1"/></svg>
        kelvanoservices@kelvanomail.example
      </span>
    </div>
  </section>

  <section class="card card--back" aria-label="Card back">
    <h2 class="section-title">Our Services</h2>
    <div class="rule title-rule"></div>

    <div class="service service--math">
      <svg viewBox="0 0 42 42" aria-hidden="true"><g fill="none" stroke="#3fae2a" stroke-width="1.8"><rect x="2" y="2" width="17" height="17" rx="3"/><rect x="23" y="2" width="17" height="17" rx="3"/><rect x="2" y="23" width="17" height="17" rx="3"/><rect x="23" y="23" width="17" height="17" rx="3"/><path d="M10.5 6.5v8M6.5 10.5h8M27.5 10.5h8M7.5 27.5l6 6M13.5 27.5l-6 6M27.5 29.5h8M27.5 33.5h8"/></g></svg>
      Math<br>Tutoring
    </div>
    <div class="service service--prep">
      <svg viewBox="0 0 42 42" aria-hidden="true"><g fill="none" stroke="#f7941d" stroke-width="1.8"><path d="M5 2h20l7 7v31H5z"/><path d="M25 2v7h7"/><rect x="9" y="13" width="4" height="4"/><rect x="9" y="21" width="4" height="4"/><rect x="9" y="29" width="4" height="4"/><path d="M16 15h11M16 23h11M16 31h8M36 14l4 3-8 16-4 2 0-4z"/></g></svg>
      NEQ &amp; BOW<br>Test Prep
    </div>
    <div class="service service--group">
      <svg viewBox="0 0 42 42" aria-hidden="true"><g fill="none" stroke="#28a3df" stroke-width="1.8"><circle cx="21" cy="21" r="19"/><circle cx="14" cy="15" r="3.5"/><circle cx="21" cy="13" r="3.5"/><circle cx="28" cy="15" r="3.5"/><path d="M8 28c0-4 3-7 6-7s6 3 6 7M22 28c0-4 3-7 6-7s6 3 6 7M14 28c0-5 3-9 7-9s7 4 7 9z"/></g></svg>
      Group and<br>Private Sessions
    </div>
    <div class="service service--school">
      <svg viewBox="0 0 42 42" aria-hidden="true"><g fill="none" stroke="#e3151d" stroke-width="1.8"><path d="M3 18l18-10 18 10M6 17v22h30V17"/><circle cx="21" cy="16" r="3.5"/><path d="M21 2v6M17 39v-9h8v9M10 24h4v5h-4zM28 24h4v5h-4zM3 39h36"/></g></svg>
      Fully Accredited<br>Private School
    </div>

    <div class="art art--study" role="img" aria-label="Illustration of a student at a desk taking an online lesson on a laptop, with shelves, backpack and a video-call screen"></div>

    <div class="contact-band">
      <span class="item">
        <svg viewBox="0 0 16 16" aria-hidden="true"><g fill="none" stroke="#f2e600" stroke-width="1.2"><circle cx="8" cy="8" r="7"/><ellipse cx="8" cy="8" rx="3" ry="7"/><path d="M1 8h14M2.2 4.5h11.6M2.2 11.5h11.6"/></g></svg>
        www.kelvanostudyhall.example
      </span>
      <span class="item">
        <svg viewBox="0 0 16 16" aria-hidden="true"><rect x="1" y="3" width="14" height="10" fill="#f2e600"/><path d="M1 3l7 6 7-6M1 13l5-5M15 13l-5-5" fill="none" stroke="#c4361c" stroke-width="1"/></svg>
        kelvanoservices@kelvanomail.example
      </span>
    </div>
  </section>

</main>
</body>
</html>
```